Health Coaching Brochure for Healthcare Practioners

I am looking to have a tri-fold brochure created marketed towards healthcare practitioners (doctors, nurses, surgeons, etc), to get them to purchase 1-on-1 health coaching from me.
I've provided the text/content (in pdf & pages), my logo, a picture of me, and two color palettes, but please also include lots of white space. I would like to design to be very clean, modern & crisp. Also include additional photos, of doctors, etc taking care of themselves & feeling happy (maybe eating healthy, maybe exercising, feeling good & happy!)
Please also see http://brightoakwellness.com and http://instagram.com/brightoakwellness for a feel of my brand.
Thank you!
Target Market(s)
Healthcare Practioners (mainly based in Los Angeles, for now)
Industry/Entity Type
Healthcare
Look and feel

```html
<!DOCTYPE html>
<html lang="en">
<head>
<meta charset="utf-8">
<title>Bright Oak Wellness – Tri-fold Brochure</title>
<link rel="stylesheet" href="https://fonts.googleapis.com/css2?family=Rubik:wght@500;700&family=Raleway:wght@300;400;600&family=Barlow+Condensed:wght@400&display=swap">
<style>
:root{
  --backdrop:#2b2b2d;
  --paper:#ffffff;
  --paper-mid:#f4f4f4;
  --maroon:#8a1c22;
  --crimson:#e0124f;
  --pill:#a31d24;
  --ink:#444;
  --ink-soft:#666;
  --sky:#2e8fd8;
  --gold:#b8860b;
  --photo-sky:#9fc3e3;
  --photo-sea:#5d88a6;
  --photo-sand:#d9cbb8;
  --photo-clinic:#dfe9f1;
  --photo-skin:#e9cdb8;
  --photo-gym:#5c5a5c;
}
*{margin:0;padding:0;box-sizing:border-box}
html,body{width:960px;height:1200px;overflow:hidden;background:var(--backdrop)}
body{position:relative;font-family:"Raleway",sans-serif;color:var(--ink)}
.sheet{position:absolute;left:108px;width:746px;height:528px;background:var(--paper);overflow:hidden;box-shadow:0 6px 18px rgba(0,0,0,.45)}
.sheet--outside{top:66px}
.sheet--inside{top:624px}
.panel{position:absolute;top:0;height:528px;overflow:hidden}
.panel--a{left:0;width:249px}
.panel--b{left:249px;width:248px;background:var(--paper-mid)}
.panel--c{left:497px;width:249px}
.abs{position:absolute}
.heading{font-family:"Rubik",sans-serif;font-weight:700;color:var(--maroon);text-transform:uppercase}
.question-title{left:16px;font-size:16px}
.question-list{left:16px;width:225px;font-size:12.3px;line-height:14.5px;color:var(--ink-soft);list-style:none}
.question-list li{margin-bottom:4px}
.question-list strong{font-weight:600;color:#333}
.photo{position:absolute}
.coach-portrait{left:83px;top:29px;width:84px;height:84px;border-radius:50%;background:linear-gradient(160deg,#6a4a3c,var(--photo-skin));border:3px solid var(--crimson)}
.coach-name{top:116px;width:100%;text-align:center;font-size:11px;color:var(--maroon)}
.coach-bio{left:20px;top:135px;width:210px;font-size:7.4px;line-height:9.6px;text-align:justify;color:var(--ink-soft)}
.motto{left:62px;top:205px;width:124px;height:100px;background:linear-gradient(135deg,#e6e6e6,#cfcfcf)}
.map-box{left:49px;top:325px;width:148px;height:72px;border:1px solid var(--maroon);border-radius:0 12px 0 12px;background:#fff;box-shadow:0 6px 8px -4px rgba(0,0,0,.25);display:flex;align-items:center;justify-content:center;font-size:12px;color:#555}
.call{top:432px;width:100%;text-align:center;font-family:"Rubik",sans-serif;font-weight:500;color:#555;font-size:21px;line-height:22px}
.call small{display:block;font-size:12.5px;line-height:15px}
.pill{background:var(--pill);color:#fff;border-radius:7px;text-align:center;font-family:"Rubik",sans-serif;box-shadow:0 3px 4px rgba(0,0,0,.25)}
.phone-pill{left:31px;top:474px;width:182px;height:24px;font-size:18px;font-weight:700;line-height:24px;letter-spacing:.5px}
.site{width:100%;text-align:center;font-size:9.6px;color:#555}
.brand-name{left:20px;top:30px;font-family:"Rubik",sans-serif;font-weight:500;font-size:19px;color:#222;letter-spacing:.3px}
.service-line{right:13px;top:384px;width:150px;text-align:right;font-size:13.4px;line-height:14.5px;color:var(--ink-soft)}
.cta-pill{left:25px;top:476px;width:199px;height:22px;font-size:12.5px;line-height:22px}
.tagline{left:16px;top:203px;font-family:"Rubik",sans-serif;font-weight:700;font-size:17.5px;line-height:20px;color:var(--sky);text-transform:uppercase}
.programs-title{left:16px;top:276px;font-size:15.5px}
.program-list{left:16px;top:299px;width:232px;list-style:none;font-size:11.7px;line-height:14px;color:#555}
.program-list li{position:relative;padding-left:11px;margin-bottom:4.5px}
.program-list li::before{content:"✓";position:absolute;left:0;top:0;color:var(--maroon);font-size:10px}
.program-list small{font-size:8px}
.integrative{left:16px;top:430px;font-size:12px;line-height:15px;color:var(--gold);text-transform:uppercase}
.access{left:16px;top:475px;display:flex;align-items:center;gap:8px;font-family:"Rubik",sans-serif;font-weight:700;font-size:17px;color:var(--sky);text-transform:uppercase}
.gut-title{top:28px;width:100%;text-align:center;font-size:17.5px;line-height:20px}
.bacteria-label{top:132px;font-family:"Barlow Condensed",sans-serif;font-size:12px;line-height:14px;text-align:center}
.bacteria-label--good{left:48px;color:#7bb24a}
.bacteria-label--bad{left:176px;color:var(--crimson)}
.gut-graphic{left:14px;top:160px;width:222px;height:270px;background:radial-gradient(ellipse at center,#a9c6ee 0 28%,#f3f6fb 29% 100%);border-radius:6px}
.ready{top:389px;width:100%;text-align:center;font-family:"Rubik",sans-serif;font-weight:500;font-size:17.5px;line-height:18.5px;color:var(--sky);text-transform:uppercase}
.schedule{top:445px;width:100%;text-align:center;font-family:"Rubik",sans-serif;font-weight:700;color:var(--maroon);text-transform:uppercase;font-size:19.5px;line-height:21px}
.schedule .accent{color:var(--gold);font-size:22px}
.schedule small{display:block;font-size:14.5px;line-height:18px}
.testi-title{top:26px;width:100%;text-align:center;font-size:17.5px}
.testi{left:13px;width:224px;font-size:8.9px;line-height:10.2px;color:var(--ink-soft);text-align:justify}
.testi p{margin-bottom:3px}
.testi cite{display:block;text-align:right;font-style:normal;font-weight:600;color:#333}
.testi-rule{left:13px;width:224px;height:1px;background:#ddd}
</style>
</head>
<body>

<!-- Outside of the brochure -->
<section class="sheet sheet--outside">

  <div class="panel panel--a">
    <h2 class="heading abs question-title" style="top:28px">Are you feeling...</h2>
    <ul class="abs question-list" style="top:50px">
      <li>overwhelmed?</li>
      <li>exhausted?</li>
      <li>struggling with food and feeling guilty about it?</li>
      <li>like you know what you <strong>SHOULD</strong> do but aren't doing it?</li>
    </ul>
    <h2 class="heading abs question-title" style="top:171px">How would it feel to ...</h2>
    <ul class="abs question-list" style="top:193px">
      <li>wake up feeling light and energized?</li>
      <li>finally get a handle on food and your cravings?</li>
      <li>reach all of your health goals and life goals?</li>
    </ul>
    <svg class="photo" style="left:0;top:330px" width="249" height="198" viewBox="0 0 249 198">
      <defs><linearGradient id="clinicA" x1="0" y1="0" x2="1" y2="1"><stop offset="0" stop-color="#cfe1ee"/><stop offset=".6" stop-color="#eef2f5"/><stop offset="1" stop-color="#f2c46a"/></linearGradient></defs>
      <path role="img" aria-label="Photo of two smiling doctors at a laptop with fresh fruit and vegetables" d="M0 60 Q110 -10 249 70 L249 198 L0 198 Z" fill="url(#clinicA)"/>
      <path d="M0 58 Q110 -14 226 48" fill="none" stroke="var(--crimson)" stroke-width="7"/>
    </svg>
  </div>

  <div class="panel panel--b">
    <div class="photo coach-portrait" role="img" aria-label="Portrait photo of the health coach"></div>
    <p class="abs coach-name">Maya Ellison</p>
    <p class="abs coach-bio">She is a personal trainer, fitness nutritionist, and holistic health coach based in Los Angeles, California. Maya helps clients improve their health, develop sustainable habits, and achieve their goals to be their best, most vibrant selves.</p>
    <div class="abs motto" role="img" aria-label="Hand-lettered motto: Trust your dopeness"></div>
    <div class="abs map-box">MAP</div>
    <p class="abs call">CALL FOR A FREE<small>15 MINUTE CONSULTATION</small></p>
    <div class="abs pill phone-pill">555-014-2270</div>
    <p class="abs site" style="top:506px">www.brightoakwellness.com</p>
  </div>

  <div class="panel panel--c">
    <p class="abs brand-name">bright oak wellness</p>
    <svg class="photo" style="left:0;top:60px" width="249" height="290" viewBox="0 0 249 290">
      <defs><linearGradient id="beach" x1="0" y1="0" x2="0" y2="1"><stop offset="0" stop-color="var(--photo-sky)"/><stop offset=".45" stop-color="var(--photo-sea)"/><stop offset=".75" stop-color="var(--photo-sand)"/><stop offset="1" stop-color="#b9a994"/></linearGradient></defs>
      <path d="M-10 150 A133 133 0 0 1 80 18" fill="none" stroke="var(--crimson)" stroke-width="6"/>
      <circle role="img" aria-label="Photo of a woman jumping joyfully on the beach" cx="122" cy="138" r="130" fill="url(#beach)"/>
      <path d="M50 240 Q120 290 225 235" fill="none" stroke="var(--crimson)" stroke-width="6"/>
    </svg>
    <svg class="photo" style="left:-14px;top:290px" width="140" height="140" viewBox="0 0 140 140">
      <circle cx="70" cy="70" r="66" fill="#fff" stroke="var(--crimson)" stroke-width="4"/>
      <circle role="img" aria-label="Photo of a smiling nutritionist at her desk with fresh fruit" cx="70" cy="70" r="62" fill="var(--photo-clinic)"/>
    </svg>
    <p class="abs service-line">Virtual &amp;<br>in-person holistic health &amp; nutrition coaching<br>los angeles, CA</p>
    <div class="abs pill cta-pill">SCHEDULE A CONSULTATION</div>
    <p class="abs site" style="top:506px">www.brightoakwellness.com/contact</p>
  </div>
</section>

<!-- Inside of the brochure -->
<section class="sheet sheet--inside">

  <div class="panel panel--a">
    <svg class="photo" style="left:0;top:0" width="249" height="190" viewBox="0 0 249 190">
      <defs><linearGradient id="clinicB" x1="0" y1="0" x2="1" y2="1"><stop offset="0" stop-color="#dde7ef"/><stop offset=".7" stop-color="#f4f6f8"/><stop offset="1" stop-color="#e9553a"/></linearGradient></defs>
      <path role="img" aria-label="Photo of a smiling nutritionist holding an apple beside fresh vegetables" d="M0 0 H249 V80 Q230 185 95 160 Q40 150 0 120 Z" fill="url(#clinicB)"/>
      <path d="M0 118 Q40 150 95 158 Q210 178 245 110" fill="none" stroke="var(--crimson)" stroke-width="7"/>
    </svg>
    <p class="abs tagline">Get healthy.<br>Feel energized.<br>Thrive!</p>
    <h2 class="heading abs programs-title">Programs &amp; Packages</h2>
    <ul class="abs program-list">
      <li>1-on-1 Health Coaching <small>(virtual or in-person)</small></li>
      <li>Group Health Coaching</li>
      <li>Specialized <small>(gluten-free, dairy-free, etc)</small><br>Meal Plans</li>
      <li>Public Speaking Education</li>
      <li>Nutrition &amp; Supplementation Counseling</li>
      <li>Wedding Preparation</li>
    </ul>
    <p class="abs integrative">Integrative nutrition &amp; health<br>coaching available, as well.</p>
    <div class="abs access">
      <svg width="36" height="36" viewBox="0 0 36 36" aria-hidden="true">
        <path d="M30 12 A14 14 0 1 0 32 20" fill="none" stroke="var(--sky)" stroke-width="3"/>
        <path d="M26 6 L31 12 L24 13" fill="none" stroke="var(--sky)" stroke-width="3"/>
        <circle cx="18" cy="18" r="10" fill="var(--sky)"/>
        <text x="18" y="21.5" text-anchor="middle" font-family="Rubik,sans-serif" font-size="9" font-weight="700" fill="#fff">24h</text>
      </svg>
      Access to trainer
    </div>
  </div>

  <div class="panel panel--b">
    <h2 class="heading abs gut-title">All disease begins<br>in the gut</h2>
    <p class="abs bacteria-label bacteria-label--good">GOOD<br>BACTERIA</p>
    <p class="abs bacteria-label bacteria-label--bad">BAD<br>BACTERIA</p>
    <div class="abs gut-graphic" role="img" aria-label="Illustration of a human body outline with the gut highlighted, linked to good bacteria on the left and bad bacteria on the right"></div>
    <p class="abs ready">Ready to make real<br>change?</p>
    <p class="abs schedule">Schedule your<br><span class="accent">15 minute</span><small>consultation today!</small></p>
  </div>

  <div class="panel panel--c">
    <h2 class="heading abs testi-title">Testimonials</h2>
    <div class="abs testi" style="top:54px">
      <p>Maya understands that everyone is different and is committed to providing a personalized health plan for her clients.</p>
      <p>She is a very passionate, caring and accountable health coach that continues to help me grow and develop my own health goals. She is wonderful to work with!</p>
      <cite>-Dana Whitlow</cite>
    </div>
    <div class="abs testi-rule" style="top:146px"></div>
    <div class="abs testi" style="top:152px">
      <p>Maya is a great trainer! After working with her I've lost more than 35 pounds. She's part trainer, part nutritionist and part life-coach. She's tough as well as supportive.</p>
      <p>She's helped me transform myself from an overweight junk food eater to a much fitter and healthier person.</p>
      <p>I highly recommend Maya to anyone and everyone.</p>
      <cite>-Rosa Merin</cite>
    </div>
    <div class="abs testi-rule" style="top:270px"></div>
    <div class="abs testi" style="top:278px">
      <p>I joined the November challenge because I had gotten way off track in my eating habits...</p>
      <p>I am so happy with the results!</p>
      <p>The fogginess is gone (as are my sugar cravings). I've found new ways to add healthy foods into my diet and (bonus) I lost five pounds the first week!</p>
      <cite>-Kate Lindqvist</cite>
    </div>
    <svg class="photo" style="left:0;top:360px" width="249" height="168" viewBox="0 0 249 168">
      <defs><linearGradient id="gym" x1="0" y1="0" x2="1" y2="1"><stop offset="0" stop-color="#8c8a8c"/><stop offset=".5" stop-color="var(--photo-skin)"/><stop offset="1" stop-color="var(--photo-gym)"/></linearGradient></defs>
      <path d="M-10 168 Q-5 30 150 22 Q220 22 249 60" fill="none" stroke="var(--crimson)" stroke-width="7"/>
      <path role="img" aria-label="Photo of a young woman training on a cable machine at the gym" d="M0 168 Q0 40 150 32 Q215 32 249 68 V168 Z" fill="url(#gym)"/>
    </svg>
  </div>
</section>

</body>
</html>
```